Kestrel electrical letter head

Require a letter head to go with our new logo for our start up company. Something fresh and professional looking, also perhaps a "ghost"image of the logo in the centre of the page. Address to go on it PO Box 58, Fernvale 7386. Web address: www.kestrel-example.net.nz

```html
<!DOCTYPE html>
<html lang="en">
<head>
<meta charset="utf-8">
<title>Kestrel Electrical – Letterhead</title>
<link rel="stylesheet" href="https://fonts.googleapis.com/css2?family=Source+Sans+3:wght@400;600;700&display=swap">
<style>
  :root {
    --green: #86bd2c;
    --green-light: #a9d132;
    --green-dark: #6aa82f;
    --blue: #2457a6;
    --ink: #3c3c3c;
    --ink-soft: #555;
    --ghost: #f3f3f3;
    --paper: #ffffff;
  }
  * { box-sizing: border-box; margin: 0; padding: 0; }
  html, body { width: 702px; height: 1200px; overflow: hidden; background: var(--paper); }
  body { font-family: "Source Sans 3", "Source Sans Pro", Arial, sans-serif; color: var(--ink); }

  .letterhead { position: relative; width: 702px; height: 1200px; background: var(--paper); overflow: hidden; }

  .corner-accent { position: absolute; top: 0; right: 0; width: 14px; height: 70px; background: var(--blue); }

  .ghost-mark { position: absolute; left: 170px; top: 450px; width: 420px; height: 420px; }

  .brand { position: absolute; left: 43px; top: 116px; display: flex; align-items: center; gap: 12px; }
  .brand-dot { width: 22px; height: 22px; border-radius: 50%; background: var(--blue); }
  .brand-name { font-size: 34px; font-weight: 700; color: var(--green-dark); letter-spacing: 0.5px; line-height: 1; }

  .contact { position: absolute; left: 520px; top: 104px; font-size: 12.5px; font-style: normal; color: var(--ink-soft); }
  .contact-title { font-size: 13.5px; font-weight: 700; color: var(--green-dark); margin-bottom: 8px; text-transform: uppercase; }
  .contact-line { display: flex; align-items: center; gap: 8px; height: 27px; white-space: nowrap; }
  .contact-icon { width: 13px; height: 13px; flex: none; }

  .date { position: absolute; right: 45px; top: 322px; font-size: 16px; font-weight: 600; color: var(--ink); }

  .recipient { position: absolute; left: 43px; top: 348px; font-size: 16px; color: var(--ink); }
  .recipient p { line-height: 39px; }

  .body-copy { position: absolute; left: 43px; top: 462px; width: 614px; font-size: 14.2px; line-height: 28px; text-align: justify; color: var(--ink-soft); }
  .body-copy p { text-indent: 40px; margin-bottom: 18px; }

  .sign-off { position: absolute; left: 43px; top: 830px; font-size: 15px; color: var(--ink-soft); }
  .signature { display: block; width: 110px; height: 44px; margin: 26px 0 10px; background: #f4f4f4; border-radius: 4px; }
  .signer-name, .signer-role { line-height: 24px; }

  .footer-band { position: absolute; left: 0; bottom: 0; width: 702px; height: 120px;
    background: linear-gradient(90deg, var(--green-dark), var(--green-light) 55%, var(--green)); }
  .footer-rule { position: absolute; left: 0; bottom: 128px; width: 702px; height: 4px; background: var(--blue); }
</style>
</head>
<body>
<main class="letterhead">

  <div class="corner-accent" aria-hidden="true"></div>

  <svg class="ghost-mark" viewBox="0 0 420 420" role="img" aria-label="Faint watermark of the company mark">
    <circle cx="210" cy="210" r="190" fill="none" stroke="var(--ghost)" stroke-width="30"/>
  </svg>

  <header>
    <div class="brand">
      <span class="brand-dot"></span>
      <span class="brand-name">Kestrel Electrical</span>
    </div>

    <address class="contact">
      <p class="contact-title">Kestrel Electrical</p>
      <p class="contact-line">
        <svg class="contact-icon" viewBox="0 0 14 14" aria-hidden="true"><circle cx="7" cy="7" r="7" fill="var(--green)"/><path d="M4.5 3.5l1.5 1.5-1 1a5 5 0 0 0 3 3l1-1 1.5 1.5-1 1.2C6.5 11 3 7.5 3.3 4.5z" fill="#fff"/></svg>
        123 - 456 - 7890
      </p>
      <p class="contact-line">
        <svg class="contact-icon" viewBox="0 0 14 14" aria-hidden="true"><circle cx="7" cy="7" r="7" fill="var(--green)"/><path d="M7 3a2.6 2.6 0 0 0-2.6 2.6C4.4 7.6 7 11 7 11s2.6-3.4 2.6-5.4A2.6 2.6 0 0 0 7 3z" fill="#fff"/></svg>
        PO Box 58, Fernvale 7386
      </p>
      <p class="contact-line">
        <svg class="contact-icon" viewBox="0 0 14 14" aria-hidden="true"><circle cx="7" cy="7" r="7" fill="var(--green)"/><circle cx="7" cy="7" r="3.6" fill="none" stroke="#fff" stroke-width="1"/><path d="M3.4 7h7.2M7 3.4v7.2" stroke="#fff" stroke-width="0.8"/></svg>
        www.kestrel-example.net.nz
      </p>
    </address>
  </header>

  <p class="date">Date: 21 May, 2018</p>

  <div class="recipient">
    <p>Your Name Here</p>
    <p>Address</p>
  </div>

  <section class="body-copy">
    <p>Lorem ipsum dolor sit amet, consectetur adilpiscing elit. Suspendisse condimenttum egestas tellus et viverra. Vestibulum euismod lacus eget nisi ornare, id laoreet tortor dapibus. Dones lacinia euismod diam, convallis termpus risus, Ut et felis termpor eros blandit feugiat ut non enim, In vestibulum ligula blandit magna blandit dictum. Sed maiesuada erat id mauris pretium, ehet congue felis interdum. A enean ultricies enim nec lorem vestibulim, nec commodo quam sagittis, Cras bibendum mauris, eget aliquit semper, libero ipaum ultricies nunc, euismod pelenteque orci risus amet nibh, Maecenas feuiat mi a metus conwallis pharetra.</p>
    <p>Duis porta turpis ut pulvinar hendrerit elit lorem behichila turpls, lacinia semper pures ros ac nisi, Sed consectetur ante scienrisque tortor pellentesque imperdiet. Pellentesque habitant morbi tristique senectus et netus et malesuacia fames ac turpis egetas. Quisque justo turpis, , varius ante nec, tincidunt pharetra telus. Donec non euismod est. Nuila in elit quis tellus mattis feugiat vitae vitae.</p>
  </section>

  <div class="sign-off">
    <p>Regards</p>
    <span class="signature" role="img" aria-label="Handwritten signature"></span>
    <p class="signer-name">Your Name Here</p>
    <p class="signer-role">Executive Director</p>
  </div>

  <div class="footer-rule" aria-hidden="true"></div>
  <div class="footer-band" aria-hidden="true"></div>

</main>
</body>
</html>
```